Silver Heron Low Voltage Systems New Van Wrap

We need a wrap for an Audio Video Company based in Orange County, CA. We design and install high end audio video systems for very expensive Residential home and large Commercial companies. We would like a design that speaks Quality, Simplicity, Clean, Elite and Professional. We are looking for a black and white design. (***All font needs to be Montserrat***) Our vans are white so graphic should be black. Less is more but we have to have the following information included:
Logo (See Attached)
Silver Heron
555-382-LINK
www.SilverHeron.example
Commercial / Residential
Data * Fiber
Audio * Video
Security Systems
Please be sure to include a side and rear view of the vehicle. Thank you.
- Montserrat
- (***All font needs to be Montserrat***)
- Less is more but we have to have the following information included:
- Logo (See Attached)
- Silver Heron
- 555-382-LINK
- www.SilverHeron.example
- Commercial / Residential
- Data * Fiber * Wi-Fi
- Audio * Video
- Security Systems

```html
<!DOCTYPE html>
<html lang="en">
<head>
<meta charset="utf-8">
<title>Silver Heron Low Voltage Systems – Van Wrap Graphics</title>
<link rel="stylesheet" href="https://fonts.googleapis.com/css2?family=Montserrat:wght@400;500;700;800&display=swap">
<style>
  :root {
    --ink: #000000;
    --paper: #ffffff;
    --canvas: #ffffff;
    --body: #f7f7f7;
    --body-line: #b9b9b9;
    --glass: #6b7072;
    --glass-light: #c9cdcf;
    --trim: #262626;
    --tire: #1c1c1c;
    --hub: #d2d2d2;
    --lamp-red: #b3262b;
    --lamp-amber: #e8a030;
    --shadow: #e2e2e2;
  }
  * { margin: 0; padding: 0; box-sizing: border-box; }
  html, body { width: 1200px; height: 1079px; overflow: hidden; background: var(--canvas); }
  body { position: relative; font-family: "Montserrat", sans-serif; color: var(--ink); }

  .vehicle-views { position: absolute; left: 0; top: 0; width: 1200px; height: 1079px; }
  .wrap-art { position: absolute; inset: 0; }
  .abs { position: absolute; }
  .center { text-align: center; white-space: nowrap; }

  .brand-mark { background: var(--ink); }
  .brand-name { font-weight: 700; letter-spacing: 0.01em; line-height: 1; }
  .tagline { font-weight: 700; line-height: 1; }
  .service-bar {
    background: var(--ink); color: var(--paper);
    display: flex; align-items: center; justify-content: center;
    font-weight: 400; white-space: nowrap; letter-spacing: 0.02em;
  }
  .phone { font-weight: 800; line-height: 1; letter-spacing: 0.01em; }
  .web { font-weight: 700; line-height: 1; }

  /* side panel */
  .side .brand-mark { left: 606px; top: 104px; width: 92px; height: 92px; }
  .side .brand-name { left: 500px; top: 234px; width: 292px; font-size: 33px; }
  .side .tagline { left: 818px; top: 87px; width: 252px; font-size: 13.5px; }
  .side .service-bar { left: 822px; width: 244px; height: 26px; font-size: 19px; }
  .side .bar-1 { top: 108px; }
  .side .bar-2 { top: 143px; }
  .side .bar-3 { top: 179px; }
  .side .phone { left: 818px; top: 213px; width: 252px; font-size: 30px; }
  .side .web { left: 818px; top: 244px; width: 252px; font-size: 16px; }

  /* rear panel */
  .rear .brand-mark { left: 188px; top: 714px; width: 64px; height: 64px; }
  .rear .brand-name { left: 124px; top: 795px; width: 180px; font-size: 21px; }
  .rear .phone { left: 326px; top: 713px; width: 172px; font-size: 18px; }
  .rear .web { left: 322px; top: 735px; width: 180px; font-size: 11.5px; }
  .rear .tagline { left: 184px; top: 839px; width: 272px; font-size: 13.5px; }
  .rear .service-bar { top: 856px; height: 15px; font-size: 9.5px; }
  .rear .bar-1 { left: 126px; width: 120px; }
  .rear .bar-2 { left: 252px; width: 120px; }
  .rear .bar-3 { left: 379px; width: 125px; }

  /* hood panel */
  .hood .brand-mark { left: 896px; top: 692px; width: 32px; height: 32px; }
  .hood .brand-name { left: 815px; top: 734px; width: 196px; font-size: 16px; }
</style>
</head>
<body>

<svg class="vehicle-views" viewBox="0 0 1200 1079" xmlns="http://www.w3.org/2000/svg">
  <!-- side view -->
  <g role="img" aria-label="Side view of white cargo van">
    <ellipse cx="600" cy="470" rx="570" ry="16" fill="var(--shadow)"/>
    <path d="M36,388 L40,268 Q60,240 180,222 L262,184 Q300,110 352,72 L1080,55 Q1112,58 1118,90 L1146,330 L1160,388 Z"
          fill="var(--body)" stroke="var(--body-line)" stroke-width="2"/>
    <polygon points="206,192 344,80 300,82 250,190" fill="var(--glass)"/>
    <polygon points="306,80 472,78 472,192 292,192" fill="var(--glass-light)" stroke="var(--glass)" stroke-width="4"/>
    <line x1="276" y1="200" x2="276" y2="390" stroke="var(--body-line)" stroke-width="2"/>
    <line x1="498" y1="66" x2="498" y2="390" stroke="var(--body-line)" stroke-width="2"/>
    <rect x="472" y="208" width="18" height="44" rx="6" fill="var(--trim)"/>
    <circle cx="656" cy="320" r="16" fill="none" stroke="var(--body-line)" stroke-width="1.5"/>
    <rect x="1114" y="118" width="24" height="68" rx="4" fill="var(--lamp-red)"/>
    <rect x="32" y="325" width="84" height="68" rx="6" fill="var(--trim)"/>
    <rect x="54" y="250" width="34" height="70" rx="8" fill="var(--trim)"/>
    <rect x="54" y="296" width="30" height="16" fill="var(--lamp-amber)"/>
    <rect x="1128" y="340" width="42" height="46" rx="6" fill="var(--trim)"/>
    <rect x="120" y="388" width="1010" height="14" fill="var(--trim)"/>
    <circle cx="208" cy="400" r="82" fill="var(--tire)"/>
    <circle cx="208" cy="400" r="44" fill="var(--hub)"/>
    <circle cx="928" cy="404" r="82" fill="var(--tire)"/>
    <circle cx="928" cy="404" r="44" fill="var(--hub)"/>
  </g>

  <!-- rear view -->
  <g role="img" aria-label="Rear view of white cargo van">
    <ellipse cx="322" cy="1030" rx="270" ry="14" fill="var(--shadow)"/>
    <rect x="112" y="940" width="48" height="88" rx="10" fill="var(--tire)"/>
    <rect x="488" y="940" width="48" height="88" rx="10" fill="var(--tire)"/>
    <path d="M78,900 L84,600 Q92,530 170,518 L480,518 Q552,530 560,600 L566,900 Z"
          fill="var(--body)" stroke="var(--body-line)" stroke-width="2"/>
    <rect x="124" y="540" width="184" height="152" rx="12" fill="var(--glass-light)" stroke="var(--trim)" stroke-width="8"/>
    <rect x="336" y="540" width="184" height="152" rx="12" fill="var(--glass-light)" stroke="var(--trim)" stroke-width="8"/>
    <line x1="320" y1="522" x2="320" y2="896" stroke="var(--body-line)" stroke-width="2"/>
    <rect x="82" y="608" width="38" height="86" rx="4" fill="var(--lamp-red)"/>
    <rect x="524" y="608" width="38" height="86" rx="4" fill="var(--lamp-red)"/>
    <rect x="336" y="752" width="128" height="58" rx="8" fill="var(--trim)"/>
    <rect x="70" y="896" width="502" height="52" rx="10" fill="var(--trim)"/>
  </g>

  <!-- front view -->
  <g role="img" aria-label="Front view of white cargo van">
    <ellipse cx="910" cy="1034" rx="270" ry="14" fill="var(--shadow)"/>
    <rect x="656" y="944" width="72" height="86" rx="10" fill="var(--tire)"/>
    <rect x="1088" y="944" width="72" height="86" rx="10" fill="var(--tire)"/>
    <path d="M660,880 L668,700 Q676,560 760,538 L1060,538 Q1150,560 1156,700 L1164,880 Z"
          fill="var(--body)" stroke="var(--body-line)" stroke-width="2"/>
    <path d="M694,680 L712,572 Q720,552 750,550 L1070,550 Q1102,552 1110,572 L1126,680 Z" fill="var(--glass-light)" stroke="var(--glass)" stroke-width="4"/>
    <rect x="638" y="616" width="46" height="56" rx="8" fill="var(--trim)"/>
    <rect x="1140" y="616" width="46" height="56" rx="8" fill="var(--trim)"/>
    <rect x="664" y="756" width="496" height="120" rx="10" fill="var(--trim)"/>
    <rect x="688" y="772" width="58" height="44" rx="6" fill="var(--hub)"/>
    <rect x="1078" y="772" width="58" height="44" rx="6" fill="var(--hub)"/>
    <rect x="660" y="822" width="106" height="26" fill="var(--lamp-amber)"/>
    <rect x="1052" y="822" width="106" height="26" fill="var(--lamp-amber)"/>
    <rect x="646" y="852" width="526" height="104" rx="14" fill="var(--trim)"/>
  </g>
</svg>

<main class="wrap-art">
  <section class="side" aria-label="Side view graphics">
    <div class="abs brand-mark" aria-hidden="true"></div>
    <div class="abs brand-name center">SILVER HERON</div>
    <div class="abs tagline center">COMMERCIAL AND RESIDENTIAL</div>
    <div class="abs service-bar bar-1">DATA | FIBER | WI-FI</div>
    <div class="abs service-bar bar-2">AUDIO | VIDEO</div>
    <div class="abs service-bar bar-3">SECURITY SYSTEMS</div>
    <div class="abs phone center">555-382-LINK</div>
    <div class="abs web center">www.SilverHeron.example</div>
  </section>

  <section class="rear" aria-label="Rear view graphics">
    <div class="abs brand-mark" aria-hidden="true"></div>
    <div class="abs brand-name center">SILVER HERON</div>
    <div class="abs phone center">555-382-LINK</div>
    <div class="abs web center">www.SilverHeron.example</div>
    <div class="abs tagline center">COMMERCIAL AND RESIDENTIAL</div>
    <div class="abs service-bar bar-1">DATA | FIBER | WI-FI</div>
    <div class="abs service-bar bar-2">AUDIO | VIDEO</div>
    <div class="abs service-bar bar-3">SECURITY SYSTEMS</div>
  </section>

  <section class="hood" aria-label="Hood graphics">
    <div class="abs brand-mark" aria-hidden="true"></div>
    <div class="abs brand-name center">SILVER HERON</div>
  </section>
</main>
</body>
</html>
```